Flyer Design Project - Nail Art

This is a flyer project for a nail saloon/cosmetics/beauty outlet. The flyer will be double-sided displaying information and/or pictures on both sides.

We would like to have the flyer in C6 format.

Prefered Background of the flyer will be black. Several image will be attached to this description (or may have been already) to help you see what we'd like to see.

FRONT SIDE: On this side we need some Text displayed; informative yet also clearly indicating that it will work as a voucher. Stylish yet professional.

BACK SIDE: Some pictures displayed to allow people to take a look at some of our work. How those pictures are displayed is entirely up to the designer. One idea that we had would be to have four pictures with the logo in the middle - however, this is entirely up to you guys.
Updates

Received a lot of great designs already, thanks!

Will provide feedback starting tomorrow; for now we'll just have a look. Thanks for your patience.

Project Deadline Extended
Reason: Only 10 days seemed a bit tight. :) We'll extend the deadline by 5 days.

Hey guys,

something important came up so I can't comment or submit feedback for two days.

Will get back to you all asap.

Cheers!

Project Deadline Extended
Reason: Extending the deadline for just a few days! Please do not submit any more designs. Thanks you!

Industry/Entity Type

Cosmetics

Requirements
Must have
• + Text below MUST be included on the front page.
+ C6 Format
+ Pictures displayed on the back
+ Logo Included

TEXT ON THE FRONT SIDE:

KL Glanzwerk - für außergewöhnliche Eyecatcher!
Mobiler Service

GUTSCHEIN

NEUANLAGE: 55.- Euro / 65.- CHF (statt 65.- Euro / 80.- CHF)
inklusive French und Verziehrung/Nailart auf 2 Nägel

AUFÜLLEN: 40,- Euro / 50.- CHF (statt 45.- Euro / 55.- CHF)

TERMINE UNTER 0664-3817056

Dieser Flyer dient als Gutschein. Am vereinbarten Termin
vorlegen!

Freundebuch: KL Glanzwerk
Mail: kl.glanzwerk@postfeld.example
Web: www.kl-glanzwerk.example

-
By designer Request - Rough english Translation of the Flyer text
-

Mobiler Service

[Voucher]
GUTSCHEIN

[Here the prices for completely new sets are listed]
[including French and Nailart on 2 nails]

[here the prices for renewing an existing set are listed]

[Contact telephone number]

[This flyer serves as a voucher. Bring it with you when you have an appointment]
vorlegen!

[Contact Details]
Freundebuch: KL Glanzwerk
Web: www.kl-glanzwerk.example
Nice to have
• FONT: Beautiful ES

NAILS labeled RED on the front page

PREFERED COLORS: Black/Red

```html
<!DOCTYPE html>
<html lang="de">
<head>
<meta charset="utf-8">
<title>KL Glanzwerk – Gutschein Flyer</title>
<link rel="stylesheet" href="https://fonts.googleapis.com/css2?family=Great+Vibes&family=Open+Sans:wght@400;600;700&family=Oswald:wght@600&display=swap">
<style>
  :root {
    --backdrop: #c9c9c9;
    --ink-black: #0e0e0e;
    --photo-top: #3a2620;
    --brand-red: #8e1b22;
    --label-red: #9a2027;
    --text-white: #f2f2f2;
    --badge-ink: #2a2a2a;
  }
  * { margin: 0; padding: 0; box-sizing: border-box; }
  html, body {
    width: 1200px; height: 900px; overflow: hidden;
    background: var(--backdrop);
    font-family: "Open Sans", Arial, sans-serif;
  }
  .flyer {
    position: absolute; left: 290px; top: 22px;
    width: 620px; height: 856px;
    background: var(--ink-black);
    overflow: hidden;
  }
  .flyer__edges { position: absolute; inset: 0; }
  .flyer__photo {
    position: absolute; left: 134px; top: 0; width: 358px; height: 400px;
    background: linear-gradient(to bottom, var(--photo-top) 0%, #241814 55%, var(--ink-black) 100%);
  }
  .tagline {
    position: absolute; left: 41px; top: 380px;
    font-family: "Great Vibes", cursive; font-size: 28px; white-space: nowrap;
    color: var(--text-white);
  }
  .tagline__brand { color: var(--brand-red); margin-right: 14px; }
  .service {
    position: absolute; left: 41px; top: 417px;
    font-size: 17px; color: var(--text-white);
  }
  .label {
    position: absolute; left: 42px;
    background: var(--label-red); color: var(--text-white);
    font-family: "Oswald", Impact, sans-serif; font-weight: 600;
    font-size: 19px; line-height: 27px; padding: 0 9px; letter-spacing: 0.3px;
  }
  .label--voucher { top: 501px; }
  .label--booking { top: 649px; }
  .offer {
    position: absolute; left: 41px;
    font-size: 14.5px; line-height: 20px; color: var(--text-white);
  }
  .offer__name { color: var(--brand-red); font-weight: 600; font-size: 17px; }
  .offer--new { top: 533px; }
  .offer--refill { top: 585px; }
  .notice {
    position: absolute; left: 41px; top: 680px;
    font-size: 15.5px; font-weight: 600; color: var(--text-white);
  }
  .social-badge {
    position: absolute; left: 42px; top: 719px; width: 178px; height: 50px;
    background: #ffffff;
    display: flex; align-items: center; gap: 10px; padding: 0 9px;
  }
  .social-badge__square { width: 30px; height: 30px; background: var(--brand-red); }
  .social-badge__name { font-size: 18px; font-weight: 600; color: var(--badge-ink); }
  .contact {
    position: absolute; left: 41px;
    font-size: 16px; color: var(--text-white); white-space: nowrap;
  }
  .contact b { font-weight: 700; }
  .contact--social { top: 771px; }
  .contact--mail { top: 794px; }
  .contact__web { margin-left: 18px; }
</style>
</head>
<body>
  <section class="flyer">
    <svg class="flyer__edges" width="620" height="856" viewBox="0 0 620 856" aria-hidden="true">
      <defs>
        <linearGradient id="edgeRed" x1="0" y1="0" x2="0" y2="1">
          <stop offset="0" stop-color="#6d1218"/>
          <stop offset="0.5" stop-color="#9a2027"/>
          <stop offset="1" stop-color="#6d1218"/>
        </linearGradient>
      </defs>
      <path d="M0 0 H20 Q40 428 16 856 H0 Z" fill="url(#edgeRed)"/>
      <path d="M620 0 H605 Q570 428 605 856 H620 Z" fill="url(#edgeRed)"/>
    </svg>

    <div class="flyer__photo" role="img" aria-label="Foto zweier Hände mit rot verzierten Nägeln"></div>

    <p class="tagline"><span class="tagline__brand">KL Glanzwerk</span> für außergewöhnliche Eyecatcher!</p>
    <p class="service">Mobiler Service</p>

    <h2 class="label label--voucher">GUTSCHEIN</h2>
    <p class="offer offer--new"><span class="offer__name">NEUANLAGE:</span> 55.- Euro / 65.- CHF (statt 65.- Euro / 80.- CHF)<br>inklusive French und Verziehrung/Nailart auf 2 Nägel</p>
    <p class="offer offer--refill"><span class="offer__name">AUFÜLLEN:</span> 40,- Euro / 50.- CHF (statt 45.- Euro / 55.- CHF)<br>inklusive French und Verziehrung/Nailart auf 2 Nägel</p>

    <h2 class="label label--booking">TERMINE UNTER 0664-3817056</h2>
    <p class="notice">Dieser Flyer dient als Gutschein. Am vereinbarten Termin vorlegen!</p>

    <div class="social-badge">
      <span class="social-badge__square"></span>
      <span class="social-badge__name">Freundebuch</span>
    </div>
    <p class="contact contact--social"><b>Freundebuch:</b> KL Glanzwerk</p>
    <p class="contact contact--mail"><b>Mail:</b> kl.glanzwerk@postfeld.example<span class="contact__web"><b>Web:</b> www.kl-glanzwerk.example</span></p>
  </section>
</body>
</html>
```